Kickbut Home Page Design built to Sell

We need a new home page layout. The website is working now but we need a refresh. Our business has slowed down since a few years ago. We need to show we build ecommerce and membership websites. Here is the page now: https://www.pelvrakwerks.graphics/new-home/

Target Market(s)

Women, solopreneurs, artists, politicians

Industry/Entity Type

Design Agency

Number of Pages Required

1 page

Font styles to use
Sans Serif

Colors
b8a6cd
fabb94
acd136
00a990

Requirements
Must have
• Video header
Section for text and Step process similar to this website: https://quillbarrowstudio.com/ [This is out sister company]
Places for images.
Call to action lead gen form and Get a quote.
The menu should show WEB, PRINT, VIDEO
Nice to have
• I LOVE this company: https://tavelmorn.com/guide/
Area for testimonials
Should not have
• We don't want a duplicate of https://quillbarrowstudio.com/

```html
<!DOCTYPE html>
<html lang="en">
<head>
<meta charset="utf-8">
<title>Pelvrakwerks — Graphics Web Video Consultants</title>
<link href="https://fonts.googleapis.com/css2?family=Oswald:wght@500;600&family=Roboto:wght@400;500;700&display=swap" rel="stylesheet">
<style>
:root{
  --lavender:#b8a6cd;
  --peach:#fabb94;
  --lime:#acd136;
  --teal:#00a990;
  --ink:#1a1a1a;
  --text:#555;
  --footer:#1e1e1e;
  --white:#fff;
}
*{box-sizing:border-box;margin:0;padding:0}
html,body{width:1200px;height:3286px;overflow:hidden}
body{position:relative;font-family:'Roboto',sans-serif;color:var(--ink);background:var(--white)}
.abs{position:absolute}
.btn{position:absolute;display:flex;align-items:center;justify-content:center;background:var(--lime);color:var(--white);font:500 15px 'Roboto',sans-serif;text-transform:uppercase;border-radius:24px;width:168px;height:44px}
h2{font:600 38px 'Oswald',sans-serif;text-transform:uppercase;color:var(--ink);letter-spacing:.3px}

/* hero */
.hero{left:0;top:0;width:1200px;height:655px;background:linear-gradient(135deg,#3a3129 0%,#2a2420 40%,#4a3a28 70%,#1f1c1a 100%)}
.hero::after{content:"";position:absolute;inset:0;background:rgba(0,0,0,.35)}
.hero-inner{position:absolute;inset:0;z-index:1}
.brand{font:600 36px 'Oswald',sans-serif;color:var(--white);letter-spacing:1px;line-height:1}
.brand small{display:block;font:500 8.5px 'Roboto',sans-serif;letter-spacing:2.4px;margin-top:4px}
.nav{left:700px;top:54px;display:flex;gap:30px;font:700 15px 'Roboto',sans-serif;color:var(--white)}
.hero-title{left:0;width:1200px;top:292px;text-align:center;font:500 44px/50px 'Oswald',sans-serif;color:var(--white);text-transform:uppercase}
.hero-sub{left:0;width:1200px;top:418px;text-align:center;font:500 17px 'Roboto',sans-serif;color:var(--white)}

/* process */
.process-photo{left:0;top:655px;width:599px;height:517px;background:linear-gradient(120deg,#cfc6b8 0%,#8a7a66 45%,#3e3530 75%,#a58a63 100%)}
.step{left:672px;width:440px}
.step-icon{position:absolute;left:0;top:0;width:58px;height:58px;border-radius:50%;background:var(--lavender);display:flex;align-items:center;justify-content:center}
.step h3{position:absolute;left:78px;top:0;font:500 17px 'Roboto',sans-serif;color:var(--ink)}
.step p{position:absolute;left:78px;top:30px;width:360px;font:400 14px/21px 'Roboto',sans-serif;color:#666}

/* work */
.work{width:311px;height:233px;overflow:hidden}
.work .shot{position:absolute;inset:0}
.work .tag{position:absolute;left:0;bottom:0;height:40px;width:215px;background:var(--lavender);clip-path:polygon(0 0,86% 0,100% 100%,0 100%);font:500 17px/40px 'Roboto',sans-serif;color:var(--ink);padding-left:25px}

/* contact */
.contact{left:0;top:1949px;width:1200px;height:431px;background:var(--peach)}
.field{position:absolute;background:var(--white);border:1px solid #eee;font:400 13px 'Roboto',sans-serif;color:#777;padding:14px 12px}

/* testimonials */
.quote{width:310px;height:190px;background:var(--white);border-radius:14px;border-top:3px solid var(--lime);box-shadow:0 6px 18px rgba(0,0,0,.08);text-align:center;padding:70px 24px 0;font:400 14px/26px 'Roboto',sans-serif;color:#666}
.avatar{width:90px;height:90px;border-radius:50%;background:linear-gradient(180deg,#d9d9d9,#9a9a9a);border:4px solid var(--white)}
.who{width:310px;text-align:center;font:500 15px 'Roboto',sans-serif;color:var(--ink)}
.who small{font:400 10px 'Roboto',sans-serif}
.stars{width:310px;text-align:center;color:#e5c100;font-size:14px;letter-spacing:1px}

/* footer */
.footer{left:0;top:2923px;width:1200px;height:363px;background:var(--footer);color:var(--white)}
.social{width:38px;height:38px;border-radius:50%;background:var(--white)}
.col h4{font:700 18px 'Roboto',sans-serif;margin-bottom:18px}
.col li{list-style:none;font:400 14px 'Roboto',sans-serif;margin-bottom:18px}
.col li::before{content:"»";color:var(--lime);margin-right:10px}
.contact-list li{list-style:none;font:400 14px/20px 'Roboto',sans-serif;margin-bottom:14px;display:flex;gap:14px}
.contact-list svg{flex:none;margin-top:3px}
.rule{left:111px;top:3206px;width:978px;height:1px;background:#333}
.copy{left:0;width:1200px;top:3233px;text-align:center;font:400 13px 'Roboto',sans-serif;color:#ddd}
</style>
</head>
<body>

<!-- Hero -->
<section class="abs hero">
  <div class="abs" role="img" aria-label="Video header: two people working together at a laptop" style="inset:0"></div>
  <div class="hero-inner">
    <div class="abs brand" style="left:110px;top:38px">PELVRAKWERKS<small>GRAPHICS WEB VIDEO CONSULTANTS</small></div>
    <nav class="abs nav"><span>WEB</span><span>PRINT</span><span>VIDEO</span></nav>
    <a class="btn" style="left:920px;top:41px">Get a quote</a>
    <svg class="abs" style="left:584px;top:232px" width="32" height="32" viewBox="0 0 32 32"><circle cx="16" cy="16" r="16" fill="#acd136"/><path d="M12 9l11 7-11 7z" fill="#1e1e1e"/></svg>
    <div class="abs hero-title">Lead generating websites that move<br>your business forward</div>
    <div class="abs hero-sub">Your Company Deserves a Website That Can Inspire People To Take Action</div>
    <a class="btn" style="left:516px;top:461px">Get a quote</a>
  </div>
</section>

<!-- Process -->
<div class="abs process-photo" role="img" aria-label="Photo: three colleagues reviewing work on a laptop in an office"></div>
<h2 class="abs" style="left:672px;top:712px">The process is simple</h2>
<div class="abs step" style="top:790px;height:80px">
  <div class="step-icon"><svg width="28" height="28" viewBox="0 0 24 24" fill="none" stroke="#fff" stroke-width="1.4"><rect x="5" y="3" width="12" height="16" rx="1"/><path d="M8 7h6M8 10h6M8 13h3M14 18l6-6 1.5 1.5-6 6H14z"/></svg></div>
  <h3>Step 1 - Tell Us Your Need</h3>
  <p>Fill out our easy questionnaire so we can understand your problems.</p>
</div>
<div class="abs step" style="top:886px;height:80px">
  <div class="step-icon"><svg width="28" height="28" viewBox="0 0 24 24" fill="none" stroke="#fff" stroke-width="1.4"><path d="M5 4l4-1 2 5-2.5 1.5a11 11 0 005 5L15 12l5 2-1 4c-8 0-14-6-14-14z"/><path d="M14 3a7 7 0 017 7M14 6a4 4 0 014 4"/></svg></div>
  <h3>Step 2 - Phone Call</h3>
  <p>Book a time to have a chat in case we have more question about your goals.</p>
</div>
<div class="abs step" style="top:982px;height:80px">
  <div class="step-icon"><svg width="28" height="28" viewBox="0 0 24 24" fill="none" stroke="#fff" stroke-width="1.4"><rect x="3" y="7" width="18" height="13" rx="1.5"/><path d="M9 7V4h6v3M3 12h18M11 12v2h2v-2"/></svg></div>
  <h3>Step 3 - Custom Quote Arrives</h3>
  <p>Once we have made your plan, we'll get to work to build and launch your new website.</p>
</div>
<a class="btn" style="left:672px;top:1084px">Get a quote</a>

<!-- Work -->
<h2 class="abs" style="left:0;width:1200px;text-align:center;top:1262px">Examples of our work</h2>
<div class="abs work" style="left:111px;top:1346px"><div class="shot" role="img" aria-label="Website mockup on laptop and tablet" style="background:linear-gradient(135deg,#5a3a28,#8b6b52 50%,#c8c0b8)"></div><div class="tag">Lorem ipsum dolor</div></div>
<div class="abs work" style="left:445px;top:1346px"><div class="shot" role="img" aria-label="Website mockup on desktop monitor and phone" style="background:linear-gradient(135deg,#b88a5a,#e6dccf 50%,#9a7048)"></div><div class="tag">Lorem ipsum dolor</div></div>
<div class="abs work" style="left:779px;top:1346px"><div class="shot" role="img" aria-label="Modern kitchen interior" style="background:linear-gradient(135deg,#e8e8e8,#6f6a63 55%,#1e1e1e)"></div><div class="tag">Lorem ipsum dolor</div></div>
<div class="abs work" style="left:111px;top:1603px"><div class="shot" role="img" aria-label="Large white house with porch" style="background:linear-gradient(180deg,#e4e6ea,#b9bec6 55%,#7a8f4a)"></div><div class="tag">Lorem ipsum dolor</div></div>
<div class="abs work" style="left:445px;top:1603px"><div class="shot" role="img" aria-label="Tudor style house among trees" style="background:linear-gradient(180deg,#e2e2e0,#8a7d70 55%,#4f5f34)"></div><div class="tag">Lorem ipsum dolor</div></div>
<div class="abs work" style="left:779px;top:1603px"><div class="shot" role="img" aria-label="Modern kitchen interior" style="background:linear-gradient(135deg,#e8e8e8,#6f6a63 55%,#1e1e1e)"></div><div class="tag">Lorem ipsum dolor</div></div>

<!-- Contact -->
<section class="abs contact">
  <h2 class="abs" style="left:0;width:1200px;text-align:center;top:36px">Contact us</h2>
  <div class="field" style="left:167px;top:101px;width:425px;height:43px">Name</div>
  <div class="field" style="left:608px;top:101px;width:426px;height:43px">Email</div>
  <div class="field" style="left:167px;top:160px;width:425px;height:43px">Phone</div>
  <div class="field" style="left:608px;top:160px;width:426px;height:43px">Company</div>
  <div class="field" style="left:167px;top:219px;width:867px;height:83px">Subject</div>
  <a class="btn" style="left:516px;top:331px">Get a quote</a>
</section>

<!-- Testimonials -->
<h2 class="abs" style="left:0;width:1185px;text-align:center;top:2458px">What our clients say</h2>
<div class="abs quote" style="left:111px;top:2588px">Dana Whitlow was great to work with and extremely knowledgeable and accessible. I especially appreciated his well thought out design process and the</div>
<div class="abs quote" style="left:445px;top:2588px">Sed ut perspiciatis unde omnis iste natus error sit voluptatem accusantium doloremque laudantium, totam rem aperiam, eaque ipsa</div>
<div class="abs quote" style="left:779px;top:2588px">Sed ut perspiciatis unde omnis iste natus error sit voluptatem accusantium doloremque laudantium, totam rem aperiam, eaque ipsa</div>
<div class="abs avatar" style="left:221px;top:2545px" role="img" aria-label="Client portrait"></div>
<div class="abs avatar" style="left:555px;top:2545px" role="img" aria-label="Client portrait"></div>
<div class="abs avatar" style="left:889px;top:2545px" role="img" aria-label="Client portrait"></div>
<div class="abs who" style="left:111px;top:2802px">Nadia Ferrow, <small>Chairman KTR</small></div>
<div class="abs who" style="left:445px;top:2802px">Lena Okafor, <small>Project Manager</small></div>
<div class="abs who" style="left:779px;top:2802px">Owen Hartle, <small>Chairman KTR</small></div>
<div class="abs stars" style="left:111px;top:2826px">★★★★★</div>
<div class="abs stars" style="left:445px;top:2826px">★★★★★</div>
<div class="abs stars" style="left:779px;top:2826px">★★★★★</div>

<!-- Footer -->
<footer class="abs footer">
  <div class="abs brand" style="left:108px;top:110px;font-size:33px">PELVRAKWERKS<small style="font-size:8px">GRAPHICS WEB VIDEO CONSULTANTS</small></div>
  <div class="abs social" style="left:143px;top:167px" aria-label="Social link"></div>
  <div class="abs social" style="left:186px;top:167px" aria-label="Social link"></div>
  <div class="abs social" style="left:229px;top:167px" aria-label="Social link"></div>
  <div class="abs social" style="left:272px;top:167px" aria-label="Social link"></div>

  <div class="abs col" style="left:419px;top:55px"><h4>Quick Links</h4><ul><li>Home</li><li>Web</li><li>Print</li><li>Video</li><li>Contact Us</li></ul></div>
  <div class="abs col" style="left:642px;top:55px"><h4>Important</h4><ul style="margin-top:4px"><li>Terms of Use</li><li>Site Map</li><li>Privacy Policy</li><li>Disclaimer</li></ul></div>
  <div class="abs" style="left:864px;top:55px">
    <h4 style="font:700 18px 'Roboto',sans-serif;margin-bottom:18px">Contact us</h4>
    <ul class="contact-list">
      <li><svg width="12" height="14" viewBox="0 0 12 14"><path d="M6 0a5 5 0 015 5c0 4-5 9-5 9S1 9 1 5a5 5 0 015-5z" fill="#acd136"/><circle cx="6" cy="5" r="2" fill="#1e1e1e"/></svg><span>17 Larkspur Ave, Brimfield<br>MA 01010</span></li>
      <li><svg width="12" height="14" viewBox="0 0 12 14"><rect x="2" y="0" width="8" height="14" rx="1.5" fill="#acd136"/><rect x="3.5" y="2" width="5" height="8" fill="#1e1e1e"/></svg><span>+41 70 555 01 23</span></li>
      <li><svg width="14" height="13" viewBox="0 0 14 13"><rect x="0" y="4" width="14" height="9" rx="1" fill="#acd136"/><rect x="3" y="0" width="8" height="5" fill="#acd136"/><rect x="3" y="7" width="8" height="2" fill="#1e1e1e"/></svg><span>+ 123 555 0147</span></li>
      <li><svg width="14" height="11" viewBox="0 0 14 11" fill="none" stroke="#acd136" stroke-width="1.4"><rect x=".7" y=".7" width="12.6" height="9.6"/><path d="M1 1l6 5 6-5"/></svg><span>dwhitlow@quillbarrowstudio.com</span></li>
    </ul>
  </div>
  <svg class="abs" style="left:1121px;top:256px" width="38" height="38" viewBox="0 0 38 38"><circle cx="19" cy="19" r="19" fill="#acd136"/><path d="M11 13h16v10H17l-4 3v-3h-2z" fill="#fff"/></svg>
</footer>
<div class="abs rule"></div>
<div class="abs copy">© 2021 pelvrakwerks &nbsp;|&nbsp; All Rights Reserved</div>

</body>
</html>
```